BrambleWorks business card

Looking for business card design that supports our company/software values. We have 2 logo designs at the moment but open to change if you think you can enhance the brand. Check out website www.brambleworks.com.au.

Target Market(s)

Education

Contact Information for Business Card

Name, title, mobile, email and website

Font styles to use
Sans Serif

Colors

Designer to choose colors to be used in the design.

Requirements
Must have
• BrambleWorks logo with tree and tagline on rear side with dark grey background colour

```html
<!DOCTYPE html>
<html lang="en">
<head>
<meta charset="utf-8">
<title>BrambleWorks business card</title>
<link rel="stylesheet" href="https://fonts.googleapis.com/css2?family=Montserrat:wght@400;500;600&display=swap">
<style>
  :root {
    --backdrop: #939393;
    --charcoal: #3c3c3c;
    --ink: #3a3a3a;
    --paper: #ffffff;
    --leaf: #4ce37c;
    --accent-red: #f2414f;
  }
  * { box-sizing: border-box; margin: 0; padding: 0; }
  html, body { width: 1200px; height: 1200px; overflow: hidden; }
  body {
    background: var(--backdrop);
    font-family: "Montserrat", sans-serif;
    position: relative;
  }
  .card {
    position: absolute;
    left: 222px;
    width: 768px;
    height: 439px;
    overflow: hidden;
  }
  /* Rear side */
  .card--rear { top: 83px; background: var(--charcoal); color: var(--paper); }
  .brand-lockup {
    position: absolute;
    display: flex;
    align-items: center;
    gap: 16px;
  }
  .brand-mark { width: 64px; height: 64px; border-radius: 50%; flex: none; }
  .brand-text { display: flex; flex-direction: column; }
  .brand-name { font-weight: 500; line-height: 1; }
  .brand-rule { height: 2px; margin: 7px 0 6px; }
  .brand-tagline { font-weight: 500; letter-spacing: .02em; }

  .card--rear .brand-lockup { left: 50%; top: 140px; transform: translateX(-50%); }
  .card--rear .brand-mark { background: var(--paper); }
  .card--rear .brand-name { font-size: 31px; color: var(--paper); }
  .card--rear .brand-rule { background: var(--accent-red); }
  .card--rear .brand-tagline { font-size: 13.5px; color: var(--paper); }

  .mission {
    position: absolute;
    top: 244px;
    left: 0; right: 0;
    text-align: center;
    font-size: 17px;
    line-height: 27.5px;
    font-weight: 500;
    text-transform: uppercase;
  }
  .web {
    position: absolute;
    color: var(--leaf);
    font-size: 14px;
    font-weight: 500;
    letter-spacing: .62em;
    text-transform: uppercase;
    white-space: nowrap;
  }
  .card--rear .web { top: 391px; left: 0; right: 0; text-align: center; padding-left: .62em; }

  /* Front side */
  .card--front { top: 627px; background: var(--paper); color: var(--ink); }
  .person { position: absolute; left: 53px; top: 42px; }
  .person-name { font-size: 30px; font-weight: 600; color: var(--leaf); line-height: 1; }
  .person-title { margin-top: 10px; font-size: 15px; font-weight: 600; letter-spacing: .45em; color: var(--ink); }

  .card--front .brand-lockup { right: 34px; top: 50px; }
  .card--front .brand-mark { background: var(--ink); width: 72px; height: 72px; }
  .card--front .brand-name { font-size: 30px; color: var(--ink); }
  .card--front .brand-rule { background: #6a6a6a; height: 1.5px; }
  .card--front .brand-tagline { font-size: 13.5px; color: var(--ink); }

  .contact-row { position: absolute; display: flex; align-items: center; }
  .contact-icon { flex: none; }
  .divider { width: 1.5px; background: var(--accent-red); flex: none; }
  .contact-lines { display: flex; flex-direction: column; }

  .phone { left: 53px; top: 172px; }
  .phone .divider { height: 64px; margin: 0 26px 0 12px; }
  .phone .contact-lines { font-size: 17.5px; letter-spacing: .14em; line-height: 28px; font-weight: 500; }

  .card--front .web { top: 262px; left: 151px; }

  .contact-band {
    position: absolute;
    left: 0; right: 0; top: 292px; bottom: 0;
    background: var(--leaf);
    color: var(--paper);
  }
  .email { left: 53px; top: 52px; }
  .email .divider { height: 42px; margin: 0 14px 0 11px; }
  .email .contact-lines { font-size: 14.5px; letter-spacing: .36em; line-height: 20px; font-weight: 500; }
  .address { left: 453px; top: 52px; }
  .address .divider { height: 42px; margin: 0 13px 0 16px; }
  .address .contact-lines { font-size: 14.5px; line-height: 21px; font-weight: 500; text-transform: uppercase; }
</style>
</head>
<body>
  <section class="card card--rear">
    <div class="brand-lockup">
      <span class="brand-mark"></span>
      <div class="brand-text">
        <span class="brand-name">BrambleWorks</span>
        <span class="brand-rule"></span>
        <span class="brand-tagline">Student Success Platform</span>
      </div>
    </div>
    <p class="mission">
      Our goal is not just to help Australian universities<br>
      close the gap - its to help Indigeneous students<br>
      become successful.
    </p>
    <p class="web">www.brambleworks.com.au</p>
  </section>

  <section class="card card--front">
    <div class="person">
      <p class="person-name">JOHN DOE</p>
      <p class="person-title">CONSULTANT</p>
    </div>

    <div class="brand-lockup">
      <span class="brand-mark"></span>
      <div class="brand-text">
        <span class="brand-name">BrambleWorks</span>
        <span class="brand-rule"></span>
        <span class="brand-tagline">Student Success Platform</span>
      </div>
    </div>

    <div class="contact-row phone">
      <svg class="contact-icon" width="35" height="35" viewBox="0 0 24 24" aria-label="Phone">
        <path fill="var(--accent-red)" d="M6.6 10.8a15.1 15.1 0 0 0 6.6 6.6l2.2-2.2a1 1 0 0 1 1-.25 11.4 11.4 0 0 0 3.6.57 1 1 0 0 1 1 1V20a1 1 0 0 1-1 1A17 17 0 0 1 3 4a1 1 0 0 1 1-1h3.5a1 1 0 0 1 1 1c0 1.25.2 2.45.57 3.57a1 1 0 0 1-.25 1z" transform="scale(-1,1) translate(-24,0)"/>
      </svg>
      <span class="divider"></span>
      <div class="contact-lines">
        <span>012-345-678</span>
        <span>012-345-678</span>
      </div>
    </div>

    <p class="web">www.brambleworks.com.au</p>

    <div class="contact-band">
      <div class="contact-row email">
        <svg class="contact-icon" width="34" height="26" viewBox="0 0 34 26" aria-label="Email">
          <rect x="1.5" y="1.5" width="31" height="23" fill="none" stroke="var(--accent-red)" stroke-width="2.5"/>
          <path d="M1.5 1.5 17 14 32.5 1.5M1.5 24.5 13 11M32.5 24.5 21 11" fill="none" stroke="var(--accent-red)" stroke-width="2"/>
        </svg>
        <span class="divider"></span>
        <div class="contact-lines">
          <span>BRAMBLEWORKS@MAIL.COM</span>
          <span>BRAMBLEWORKS@MAIL.COM</span>
        </div>
      </div>
      <div class="contact-row address">
        <svg class="contact-icon" width="24" height="34" viewBox="0 0 24 34" aria-label="Location">
          <path fill="var(--accent-red)" d="M12 0C5.4 0 0 5.2 0 11.7 0 20 12 34 12 34s12-14 12-22.3C24 5.2 18.6 0 12 0zm0 16a4.5 4.5 0 1 1 0-9 4.5 4.5 0 0 1 0 9z"/>
        </svg>
        <span class="divider"></span>
        <div class="contact-lines">
          <span>BrambleWorks address goes</span>
          <span>here</span>
        </div>
      </div>
    </div>
  </section>
</body>
</html>
```